iron deficiency anemia - educational reference paper

looking for an educational paper/poster 8x11 or no larger than 11x14 that lists the most common foods with pictures and limited words a super rough outline attached - I wrote the words of the pictures (but would like to have the actual pictures of these items) I would like in roughly the same order
for the pictures for fatigue, headache....can be drawings or cartoons
double sided or single sided (which ever fits) see attached for categories (3 of them)

Target Market(s)

educational for people with limited education - thus not much wording

Requirements
Must have
• pictures, simple design

```html
<!DOCTYPE html>
<html lang="en">
<head>
<meta charset="utf-8">
<title>Iron Deficiency Anemia – Reference Sheets</title>
<link href="https://fonts.googleapis.com/css2?family=Montserrat:wght@500;600;700;800&display=swap" rel="stylesheet">
<style>
  :root{
    --stage:#6f6f79;
    --paper:#ffffff;
    --red:#a8172c;
    --red-deep:#6b0b18;
    --red-bright:#c8102e;
    --ink:#1b1b1b;
    --label:#111111;
    --swoosh:#d9d9dc;
  }
  *{box-sizing:border-box;margin:0;padding:0}
  html,body{width:1200px;height:1200px;overflow:hidden}
  body{background:var(--stage);font-family:"Montserrat",sans-serif;position:relative}
  .sheet{position:absolute;top:228px;height:714px;background:var(--paper);overflow:hidden;box-shadow:0 2px 8px rgba(0,0,0,.25)}
  .sheet--foods{left:32px;width:552px}
  .sheet--symptoms{left:604px;width:558px}

  /* Foods sheet */
  .foods-header{position:absolute;left:0;top:0;width:552px;height:260px}
  .foods-title{position:absolute;left:16px;top:10px;color:#fff;font-weight:800;font-size:40px;line-height:1.05;letter-spacing:.5px}
  .portrait{position:absolute;left:335px;top:57px;width:186px;height:186px;border-radius:50%;border:7px solid #c9c9cc;background:radial-gradient(circle at 50% 40%,#f1e4dc,#d9b6a4 70%,#c98a6a)}
  .foods-heading{position:absolute;left:10px;top:158px;color:var(--red-bright);font-weight:700;font-size:24px;line-height:1.1}
  .foods-rule{position:absolute;left:10px;top:246px;width:238px;height:2px;background:var(--red-bright)}
  .foods-rule::after{content:"";position:absolute;right:-3px;top:-3px;width:8px;height:8px;border-radius:50%;background:var(--red-bright)}
  .food-column{position:absolute;top:276px;list-style:none}
  .food-column li{display:flex;align-items:center;height:28.8px;font-size:9.5px;font-weight:500;color:var(--ink);text-transform:uppercase;white-space:nowrap}
  .food-icon{width:24px;height:24px;border-radius:50%;margin-right:11px;flex:none;background:var(--c,#bbb)}
  .col-1{left:20px}.col-2{left:146px}.col-3{left:282px}.col-4{left:418px}
  .produce{position:absolute;right:0;bottom:16px;width:152px;height:58px;border-radius:30px 0 0 0;background:linear-gradient(90deg,#d8a23a,#5b9b3a 45%,#3f7f2e 70%,#c23a2a)}
  .foods-band{position:absolute;left:0;bottom:0;width:100%;height:16px;background:var(--red)}

  /* Symptoms sheet */
  .symptoms-header{position:absolute;left:0;top:0;width:100%;height:60px;background:linear-gradient(90deg,var(--red-deep),var(--red) 60%,var(--red-deep));color:#fff;text-align:center;font-size:27px;font-weight:600;line-height:60px;letter-spacing:.5px}
  .symptoms-header b{font-weight:800}
  .symptom-photo{position:absolute;background:linear-gradient(180deg,#ececec,#cfcfd2)}
  .symptom-photo--round{border-radius:50%;background:radial-gradient(circle at 50% 45%,#d9c3b8,#8a7a74)}
  .symptom-label{position:absolute;z-index:2;display:flex;align-items:center;height:22px}
  .tick{width:22px;height:22px;flex:none;margin-right:6px}
  .label-box{background:var(--label);color:#fff;font-weight:700;font-size:16px;height:20px;line-height:20px;padding:0 10px;letter-spacing:.5px;white-space:nowrap}
  .signs-art{position:absolute;z-index:0;left:0;top:384px;width:558px;height:330px}
  .signs-title{position:absolute;z-index:2;left:20px;top:578px;color:#fff;font-weight:800;font-size:35px;line-height:38px}
  .signs-rule{position:absolute;z-index:2;left:0;top:664px;width:214px;height:2px;background:var(--red-bright)}
  .signs-rule::after{content:"";position:absolute;right:-3px;top:-3px;width:8px;height:8px;border-radius:50%;background:var(--red-bright)}
  .signs-panel{position:absolute;z-index:2;left:231px;top:508px;width:308px;height:166px;background:#fff;padding:6px;display:grid;grid-template-columns:1fr 1fr;gap:6px}
  .sign-photo{background:linear-gradient(135deg,#e6cfc4,#b98f80)}
  .sign-photo--eye{background:linear-gradient(135deg,#c6524a,#f0d6cf 60%,#9bb0b8)}
  .sign-photo--tongue{background:linear-gradient(135deg,#f3e2da,#d99a90)}
  .symptoms-band{position:absolute;z-index:2;left:0;bottom:0;width:100%;height:14px;background:var(--red-deep)}
</style>
</head>
<body>

<section class="sheet sheet--foods">
  <svg class="foods-header" viewBox="0 0 552 260" role="img" aria-label="Red blood cells backdrop">
    <defs>
      <radialGradient id="cellsA" cx="0.7" cy="0.3" r="0.9">
        <stop offset="0" stop-color="#c21f33"/><stop offset="1" stop-color="#5e0914"/>
      </radialGradient>
    </defs>
    <rect width="552" height="260" fill="url(#cellsA)"/>
    <path d="M0 112 C150 70 330 150 552 72 L552 260 L0 260Z" fill="#d9d9dc"/>
    <path d="M0 128 C150 86 330 166 552 92 L552 260 L0 260Z" fill="#ffffff"/>
  </svg>
  <h1 class="foods-title">IRON DEFICIENCY<br>ANEMIA</h1>
  <div class="portrait" role="img" aria-label="Photo of a person holding an apple and a pear"></div>
  <h2 class="foods-heading">Common<br>Foods in<br>Your Community</h2>
  <div class="foods-rule"></div>

  <ul class="food-column col-1">
    <li><span class="food-icon" style="--c:#cfc9bd" role="img" aria-label="Sheep photo"></span>Sheep/Lamb</li>
    <li><span class="food-icon" style="--c:#9a948c" role="img" aria-label="Goose photo"></span>Goose</li>
    <li><span class="food-icon" style="--c:#6f8fb5" role="img" aria-label="Whale photo"></span>Whale</li>
    <li><span class="food-icon" style="--c:#7fa43c" role="img" aria-label="Winged bean photo"></span>Winged Bean</li>
    <li><span class="food-icon" style="--c:#a88f6e" role="img" aria-label="Rice bran photo"></span>Rice Bran</li>
    <li><span class="food-icon" style="--c:#e4e0d6" role="img" aria-label="White bean photo"></span>White Bean</li>
    <li><span class="food-icon" style="--c:#b29581" role="img" aria-label="Pig photo"></span>Pig/Pork</li>
    <li><span class="food-icon" style="--c:#7b2a3a" role="img" aria-label="Kidney bean photo"></span>Kidney Bean</li>
    <li><span class="food-icon" style="--c:#d8c6a4" role="img" aria-label="Cowpea photo"></span>Cowpea</li>
    <li><span class="food-icon" style="--c:#2a2626" role="img" aria-label="Black bean photo"></span>Black Bean</li>
    <li><span class="food-icon" style="--c:#6b8c3a" role="img" aria-label="Mung bean photo"></span>Mung Bean</li>
    <li><span class="food-icon" style="--c:#8a6a3a" role="img" aria-label="Natto photo"></span>Natto</li>
    <li><span class="food-icon" style="--c:#8b5a34" role="img" aria-label="Teff photo"></span>Teff</li>
    <li><span class="food-icon" style="--c:#d9b676" role="img" aria-label="Amaranth photo"></span>Amaranth</li>
  </ul>

  <ul class="food-column col-2">
    <li><span class="food-icon" style="--c:#4f8f2e" role="img" aria-label="Yardlong bean photo"></span>Yardlong Bean</li>
    <li><span class="food-icon" style="--c:#c4321f" role="img" aria-label="Chili bean photo"></span>Chili/Pink Bean</li>
    <li><span class="food-icon" style="--c:#c9782e" role="img" aria-label="Lentil photo"></span>Lentil</li>
    <li><span class="food-icon" style="--c:#d9b23a" role="img" aria-label="Yellow bean photo"></span>Yellow Bean</li>
    <li><span class="food-icon" style="--c:#6f9a8a" role="img" aria-label="Duck photo"></span>Duck</li>
    <li><span class="food-icon" style="--c:#c9d98a" role="img" aria-label="Lima bean photo"></span>Lima Bean</li>
    <li><span class="food-icon" style="--c:#7a8f4a" role="img" aria-label="Chicken photo"></span>Chicken</li>
    <li><span class="food-icon" style="--c:#a79d90" role="img" aria-label="Clams photo"></span>Clams</li>
    <li><span class="food-icon" style="--c:#d9762a" role="img" aria-label="Pumpkin seed photo"></span>Pumpkin Seed</li>
    <li><span class="food-icon" style="--c:#8c8c8c" role="img" aria-label="Squab photo"></span>Squab</li>
    <li><span class="food-icon" style="--c:#8a8f5a" role="img" aria-label="Pigeon pea photo"></span>Pigeon Pea</li>
    <li><span class="food-icon" style="--c:#b8693a" role="img" aria-label="Fava bean photo"></span>Fava Bean</li>
    <li><span class="food-icon" style="--c:#a8a8a8" role="img" aria-label="Sesame seed photo"></span>Sesame Seed</li>
    <li><span class="food-icon" style="--c:#8f2a22" role="img" aria-label="Adzuki bean photo"></span>Aduzki Bean</li>
  </ul>

  <ul class="food-column col-3">
    <li><span class="food-icon" style="--c:#b08a78" role="img" aria-label="Cranberry bean photo"></span>Cranberry Bean</li>
    <li><span class="food-icon" style="--c:#efe6d4" role="img" aria-label="Masa photo"></span>Masa</li>
    <li><span class="food-icon" style="--c:#d9ab2a" role="img" aria-label="Split peas photo"></span>Split Peas</li>
    <li><span class="food-icon" style="--c:#cfcfcf" role="img" aria-label="Cuttlefish photo"></span>Cuttlefish</li>
    <li><span class="food-icon" style="--c:#8a5a2a" role="img" aria-label="Bear photo"></span>Bear</li>
    <li><span class="food-icon" style="--c:#e0a81f" role="img" aria-label="Sunflower seed photo"></span>Sunflower Seed</li>
    <li><span class="food-icon" style="--c:#c07a34" role="img" aria-label="Bagel photo"></span>Bagel</li>
    <li><span class="food-icon" style="--c:#a4a9b0" role="img" aria-label="Sardines photo"></span>Sardines</li>
    <li><span class="food-icon" style="--c:#d9c23a" role="img" aria-label="Chickpeas photo"></span>Chickpeas</li>
    <li><span class="food-icon" style="--c:#e89a7a" role="img" aria-label="Shrimp photo"></span>Shrimp</li>
    <li><span class="food-icon" style="--c:#3f8a2e" role="img" aria-label="Spinach photo"></span>Spinach</li>
    <li><span class="food-icon" style="--c:#7a2a4a" role="img" aria-label="Beet photo"></span>Beet</li>
    <li><span class="food-icon" style="--c:#5f8f34" role="img" aria-label="Brussels sprouts photo"></span>Brussle Sprouts</li>
    <li><span class="food-icon" style="--c:#d8c0a0" role="img" aria-label="Egg photo"></span>Egg</li>
  </ul>

  <ul class="food-column col-4">
    <li><span class="food-icon" style="--c:#3f7a2a" role="img" aria-label="Collard greens photo"></span>Collard Greens</li>
    <li><span class="food-icon" style="--c:#5a4a34" role="img" aria-label="Mushrooms photo"></span>Mushrooms</li>
    <li><span class="food-icon" style="--c:#b88a4a" role="img" aria-label="Nuts photo"></span>Nuts</li>
    <li><span class="food-icon" style="--c:#c9a46a" role="img" aria-label="Potatoes photo"></span>Potatoes</li>
    <li><span class="food-icon" style="--c:#e0c07a" role="img" aria-label="Tortilla photo"></span>Tortilla</li>
    <li><span class="food-icon" style="--c:#a8623a" role="img" aria-label="Turkey photo"></span>Turkey</li>
    <li><span class="food-icon" style="--c:#2a2a34" role="img" aria-label="Blackberry photo"></span>Blackberry</li>
    <li><span class="food-icon" style="--c:#4a8a34" role="img" aria-label="Broccoli photo"></span>Broccoli</li>
    <li><span class="food-icon" style="--c:#e0701f" role="img" aria-label="Carrot photo"></span>Carrot</li>
    <li><span class="food-icon" style="--c:#e8e2c8" role="img" aria-label="Cauliflower photo"></span>Cauliflower</li>
    <li><span class="food-icon" style="--c:#7a6a5a" role="img" aria-label="Halibut photo"></span>Halibut</li>
    <li><span class="food-icon" style="--c:#d42a1f" role="img" aria-label="Tomato photo"></span>Tomatoe</li>
  </ul>

  <div class="produce" role="img" aria-label="Photo of fresh vegetables"></div>
  <div class="foods-band"></div>
</section>

<section class="sheet sheet--symptoms">
  <h2 class="symptoms-header">SYMPTOMS OF <b>ANEMIA</b></h2>

  <div class="symptom-photo" style="left:50px;top:76px;width:96px;height:112px" role="img" aria-label="Photo of a tired person"></div>
  <div class="symptom-photo symptom-photo--round" style="left:214px;top:74px;width:118px;height:118px" role="img" aria-label="Photo of a person with a headache"></div>
  <div class="symptom-photo symptom-photo--round" style="left:390px;top:74px;width:118px;height:118px" role="img" aria-label="Photo of a dizzy person"></div>
  <div class="symptom-photo" style="left:78px;top:236px;width:110px;height:116px" role="img" aria-label="Photo of a person with blurry vision"></div>
  <div class="symptom-photo" style="left:342px;top:242px;width:134px;height:110px" role="img" aria-label="Photo of a person with muscle weakness"></div>

  <svg class="signs-art" viewBox="0 0 558 330" role="img" aria-label="Red blood cells backdrop">
    <defs>
      <radialGradient id="cellsB" cx="0.75" cy="0.35" r="0.9">
        <stop offset="0" stop-color="#c21f33"/><stop offset="1" stop-color="#5a0812"/>
      </radialGradient>
    </defs>
    <rect width="558" height="330" fill="url(#cellsB)"/>
    <path d="M0 0 H558 V24 C420 16 210 70 0 156 Z" fill="#d9d9dc"/>
    <path d="M0 0 H558 V8 C420 0 210 54 0 138 Z" fill="#ffffff"/>
  </svg>

  <div class="symptom-label" style="left:18px;top:198px">
    <svg class="tick" viewBox="0 0 22 22" aria-hidden="true"><rect x="1.5" y="4.5" width="16" height="16" fill="#fff" stroke="#c8102e" stroke-width="2.5"/><path d="M5 12l4 5 11-15" fill="none" stroke="#c8102e" stroke-width="3.2"/></svg>
    <span class="label-box">FATIGUE</span>
  </div>
  <div class="symptom-label" style="left:184px;top:198px">
    <svg class="tick" viewBox="0 0 22 22" aria-hidden="true"><rect x="1.5" y="4.5" width="16" height="16" fill="#fff" stroke="#c8102e" stroke-width="2.5"/><path d="M5 12l4 5 11-15" fill="none" stroke="#c8102e" stroke-width="3.2"/></svg>
    <span class="label-box" style="width:150px">HEADACHE</span>
  </div>
  <div class="symptom-label" style="left:368px;top:198px">
    <svg class="tick" viewBox="0 0 22 22" aria-hidden="true"><rect x="1.5" y="4.5" width="16" height="16" fill="#fff" stroke="#c8102e" stroke-width="2.5"/><path d="M5 12l4 5 11-15" fill="none" stroke="#c8102e" stroke-width="3.2"/></svg>
    <span class="label-box" style="width:150px">DIZZINESS</span>
  </div>
  <div class="symptom-label" style="left:18px;top:359px">
    <svg class="tick" viewBox="0 0 22 22" aria-hidden="true"><rect x="1.5" y="4.5" width="16" height="16" fill="#fff" stroke="#c8102e" stroke-width="2.5"/><path d="M5 12l4 5 11-15" fill="none" stroke="#c8102e" stroke-width="3.2"/></svg>
    <span class="label-box" style="width:186px">BLURRY VISION</span>
  </div>
  <div class="symptom-label" style="left:280px;top:359px">
    <svg class="tick" viewBox="0 0 22 22" aria-hidden="true"><rect x="1.5" y="4.5" width="16" height="16" fill="#fff" stroke="#c8102e" stroke-width="2.5"/><path d="M5 12l4 5 11-15" fill="none" stroke="#c8102e" stroke-width="3.2"/></svg>
    <span class="label-box" style="width:214px">MUSCLE WEAKNESS</span>
  </div>

  <h2 class="signs-title">SIGNS OF<br>ANEMIA</h2>
  <div class="signs-rule"></div>
  <div class="signs-panel">
    <div class="sign-photo" role="img" aria-label="Photo of pale fingernails"></div>
    <div class="sign-photo sign-photo--eye" role="img" aria-label="Photo of a pale inner eyelid"></div>
    <div class="sign-photo" role="img" aria-label="Photo of pale hands"></div>
    <div class="sign-photo sign-photo--tongue" role="img" aria-label="Photo of a pale tongue"></div>
  </div>
  <div class="symptoms-band"></div>
</section>

</body>
</html>
```